Bright Sprouts Newcastle Event Flyer

This flyer is to advertise a gathering of experts who each be speaking on different aspects of child health and development called on Bright Sprouts Newcastle.

Can it please include the logo attached.

Details in include:

July 25th 2015
12-4pm

Industry/Entity Type

Health

```html
<!DOCTYPE html>
<html lang="en">
<head>
<meta charset="utf-8">
<title>Bright Sprouts Newcastle Event Flyer</title>
<link rel="stylesheet" href="https://fonts.googleapis.com/css2?family=Cherry+Swash:wght@700&family=Source+Sans+3:wght@600;700&family=Arimo:wght@700&display=swap">
<style>
  :root {
    --backdrop: #ece8e1;
    --paper-top: #fdfcf4;
    --paper-bottom: #fbe9b4;
    --brand-orange: #ec6a2c;
    --brand-blue: #3d86c8;
    --heading-ink: #353535;
    --pill-blue: #1d6fb7;
    --pill-text: #ffffff;
    --url-ink: #3a3a3a;
    --photo-sky: #b9dcf2;
    --photo-warm: #f3d9a6;
    --swirl-pink: #f2c6d0;
  }
  html, body {
    margin: 0;
    padding: 0;
    width: 941px;
    height: 1200px;
    overflow: hidden;
    background: var(--backdrop);
  }
  .flyer {
    position: absolute;
    left: 89px;
    top: 104px;
    width: 722px;
    height: 1014px;
    overflow: hidden;
    background: linear-gradient(180deg, var(--paper-top) 0%, var(--paper-top) 45%, var(--paper-bottom) 100%);
    box-shadow: 0 4px 14px rgba(0,0,0,0.25);
  }
  .brand {
    position: absolute;
    left: 56px;
    top: 72px;
    display: flex;
    align-items: center;
    gap: 12px;
  }
  .brand-dot {
    width: 22px;
    height: 22px;
    border-radius: 50%;
    background: var(--brand-blue);
  }
  .brand-name {
    font-family: "Source Sans 3", sans-serif;
    font-weight: 700;
    font-size: 40px;
    color: var(--brand-orange);
    line-height: 1;
  }
  .hero {
    position: absolute;
    left: 0;
    top: 0;
  }
  .headline {
    position: absolute;
    left: 0;
    width: 100%;
    top: 676px;
    margin: 0;
    text-align: center;
    font-family: "Cherry Swash", serif;
    font-weight: 700;
    font-size: 52px;
    color: var(--heading-ink);
    line-height: 1;
  }
  .summary {
    position: absolute;
    left: 90px;
    width: 542px;
    top: 758px;
    margin: 0;
    text-align: center;
    font-family: "Source Sans 3", sans-serif;
    font-weight: 700;
    font-size: 27px;
    line-height: 36px;
    color: var(--brand-orange);
  }
  .swirls {
    position: absolute;
    left: 0;
    top: 816px;
  }
  .date-pill {
    position: absolute;
    left: 106px;
    top: 893px;
    width: 502px;
    height: 40px;
    border-radius: 12px;
    background: var(--pill-blue);
    color: var(--pill-text);
    font-family: "Arimo", sans-serif;
    font-weight: 700;
    font-size: 27px;
    line-height: 40px;
    text-align: center;
    letter-spacing: 0.3px;
  }
  .website {
    position: absolute;
    left: 0;
    width: 100%;
    top: 955px;
    text-align: center;
    font-family: "Source Sans 3", sans-serif;
    font-weight: 700;
    font-size: 24px;
    color: var(--url-ink);
  }
</style>
</head>
<body>
  <main class="flyer">
    <svg class="hero" width="722" height="680" viewBox="0 0 722 680" role="img" aria-label="Photograph of two smiling schoolgirls at a classroom desk with coloured pencils">
      <defs>
        <linearGradient id="heroFill" x1="0" y1="0" x2="0" y2="1">
          <stop offset="0" stop-color="var(--photo-sky)"/>
          <stop offset="1" stop-color="var(--photo-warm)"/>
        </linearGradient>
      </defs>
      <circle cx="270" cy="390" r="250" fill="url(#heroFill)"/>
      <circle cx="565" cy="335" r="225" fill="url(#heroFill)"/>
      <path d="M30 380 A250 250 0 0 1 300 130" fill="none" stroke="var(--brand-blue)" stroke-width="1.5" opacity="0.6"/>
      <path d="M45 470 A252 252 0 0 0 330 650" fill="none" stroke="var(--brand-blue)" stroke-width="1.5" opacity="0.6"/>
      <path d="M540 112 A228 228 0 0 1 722 200" fill="none" stroke="var(--brand-blue)" stroke-width="1.5" opacity="0.5"/>
    </svg>

    <div class="brand">
      <span class="brand-dot"></span>
      <span class="brand-name">Bright Sprouts</span>
    </div>

    <h1 class="headline">Newcastle Event</h1>
    <p class="summary">Gathering of experts who each be speaking on different aspects of child health and development</p>

    <svg class="swirls" width="170" height="120" viewBox="0 0 170 120" role="img" aria-label="Decorative pink concentric circle pattern">
      <circle cx="80" cy="50" r="42" fill="var(--swirl-pink)" opacity="0.6"/>
      <circle cx="28" cy="92" r="22" fill="var(--swirl-pink)" opacity="0.6"/>
    </svg>

    <div class="date-pill">July 25th 2015. Time: 12-4pm</div>
    <div class="website">www.bright-sprouts.com.au</div>
  </main>
</body>
</html>
```